Business Card Design Project

We need a business card for our IT services provider business. We provide services to small and medium business, and would like something that reflects the color scheme / branding on our recently updated website - www.larkbyte.com.au

The card type we have chosen is a matte laminated double sided configuration at 86mm x 54mm on 350 GSM cardboard.
Updates

Target Market(s)

Small and Medium Business owners

Industry/Entity Type

Business

Requirements
Must have
• *Details on all cards*

Company Name: LarkByte IT Pty Ltd
ABN: 62 385 219 604
Address: 47-49 Marrow Street, Kelbrook Vale, Victoria 3150
Phone: 1300 LARK BY
Fax: 03 9417 6209
Website: www.larkbyte.com.au
Logo/Handprint Icon

*Person Specific*

```html
<!DOCTYPE html>
<html lang="en">
<head>
<meta charset="utf-8">
<title>LarkByte IT – Business Card</title>
<link rel="stylesheet" href="https://fonts.googleapis.com/css2?family=Roboto+Condensed:wght@400;700&display=swap">
<style>
  :root {
    --backdrop: #e8e8e8;
    --card-white: #ffffff;
    --card-blue: #1f6db3;
    --ink: #2b2b2b;
    --ink-soft: #4a4a4a;
    --brand-navy: #16263a;
    --brand-blue: #2a6db5;
    --on-blue: #ffffff;
    --shadow: rgba(0, 0, 0, 0.18);
  }
  * { box-sizing: border-box; margin: 0; padding: 0; }
  html, body {
    width: 1141px;
    height: 1200px;
    overflow: hidden;
    background: var(--backdrop);
    font-family: "Roboto Condensed", "Arial Narrow", sans-serif;
  }
  .card-sheet {
    position: relative;
    width: 1141px;
    height: 1200px;
  }
  .card {
    position: absolute;
    top: 218px;
    width: 480px;
    height: 764px;
    overflow: hidden;
    box-shadow: 0 6px 18px var(--shadow);
  }
  .card--front { left: 60px; background: var(--card-white); }
  .card--back  { left: 600px; background: var(--card-blue); }

  /* content is set landscape and turned to read bottom-to-top */
  .card-face {
    position: absolute;
    left: 50%;
    top: 50%;
    width: 764px;
    height: 480px;
    transform: translate(-50%, -50%) rotate(-90deg);
  }

  .brand {
    position: absolute;
    left: 60px;
    top: 150px;
    display: flex;
    align-items: center;
    gap: 18px;
  }
  .brand-mark {
    width: 30px;
    height: 30px;
    background: var(--brand-blue);
  }
  .brand-name {
    font-size: 66px;
    font-weight: 400;
    letter-spacing: 1px;
    color: var(--brand-navy);
  }

  .company-details {
    position: absolute;
    left: 60px;
    bottom: 46px;
    font-size: 22px;
    line-height: 1.32;
    color: var(--ink-soft);
    list-style: none;
  }
  .company-details .label { font-weight: 700; color: var(--ink); margin-right: 6px; }
  .company-details .gap { display: inline-block; width: 34px; }
  .company-details .web-name { font-weight: 700; color: var(--brand-blue); }

  .contact-person {
    position: absolute;
    left: 330px;
    top: 214px;
    color: var(--on-blue);
    font-size: 24px;
    line-height: 1.35;
    list-style: none;
  }
  .contact-person .surname { font-weight: 700; }
</style>
</head>
<body>
<main class="card-sheet">
  <section class="card card--front" aria-label="Card front">
    <div class="card-face">
      <div class="brand">
        <span class="brand-mark"></span>
        <span class="brand-name">LarkByte IT</span>
      </div>
      <ul class="company-details">
        <li>ABN: 62 385 219 604</li>
        <li>47-49 Marrow Street, Kelbrook Vale, Victoria 3150</li>
        <li><span class="label">P</span>1300 LARK BY<span class="gap"></span><span class="label">F</span>03 9417 6209</li>
        <li>www.<span class="web-name">LarkByte</span>.com.au</li>
      </ul>
    </div>
  </section>

  <section class="card card--back" aria-label="Card back">
    <div class="card-face">
      <ul class="contact-person">
        <li>Dana <span class="surname">Whitlow</span></li>
        <li>PHN-NUM-XXXX</li>
        <li>dana@larkbyte.com.au</li>
      </ul>
    </div>
  </section>
</main>
</body>
</html>
```